Clear plastic business card for window cleaning company

hi guys
i run a window cleaning company and need a new business card design. i want a design for a clear or frosted plastic business card.
i have uploaded my logo and a silhouette of a guy abseiling
thought maybe the clear card could simulate a clear window or windows.
the abseiler doesn't have to be used but i think it looks good if it could be incorporated into the design as we clean all windows from houses to high rise buildings

my name is dean marlow
phone number is 0438 602 917
email dean@glazoria.net.au
web www.glazoria.net.au
services offered are
window cleaning
high pressure cleaning
building washdowns
gutter cleaning
difficult access specialist
abseiling
elevated work platforms
commercial/domestic/high-rise

Contact Information for Business Card

my name is dean marlow
email dean@glazoria.net.au
web www.glazoria.net.au
services offered are
window cleaning
high pressure cleaning
building washdowns
gutter cleaning
abseiling
elevated work platforms

Requirements
Must have
• cool design that stands out i want the clear or frosted card to simulate a window to get a stand out effect

```html
<!DOCTYPE html>
<html lang="en">
<head>
<meta charset="utf-8">
<title>Glazoria Services – Business Card</title>
<link rel="stylesheet" href="https://fonts.googleapis.com/css2?family=Arimo:wght@400;700&display=swap">
<style>
  :root {
    --page: #e6e9ed;
    --frost: rgba(244, 247, 250, 0.92);
    --frost-edge: #cfd6de;
    --sky-top: #2f7fc8;
    --sky-mid: #5ea3dc;
    --sky-fade: rgba(150, 196, 232, 0.35);
    --navy: #123a66;
    --navy-deep: #0b2746;
    --bar: #1d2b38;
    --accent-green: #8dc63f;
    --ink: #1f4f82;
    --tick: #2a7ac4;
    --figure: #3c4650;
  }
  * { box-sizing: border-box; margin: 0; padding: 0; }
  html, body {
    width: 847px; height: 1200px; overflow: hidden;
    background: var(--page);
    font-family: "Arimo", Arial, sans-serif;
  }
  .sheet {
    width: 847px; height: 1200px;
    display: flex; flex-direction: column; align-items: center; justify-content: center;
    gap: 70px;
  }
  .card {
    position: relative;
    width: 700px; height: 427px;
    background: var(--frost);
    border: 1px solid var(--frost-edge);
    border-radius: 6px;
    overflow: hidden;
    box-shadow: 0 6px 18px rgba(20, 40, 60, 0.15);
  }

  /* Front */
  .card-front .sky-band {
    position: absolute; left: 0; top: 0; right: 0; height: 250px;
    background: linear-gradient(180deg, var(--sky-top) 0%, var(--sky-mid) 55%, var(--sky-fade) 100%);
  }
  .brand-block {
    position: absolute; right: 40px; top: 34px;
    width: 250px; padding: 16px 18px;
    background: var(--navy-deep);
    display: flex; flex-direction: column; gap: 4px;
  }
  .brand-name { color: #fff; font-weight: 700; font-size: 34px; letter-spacing: 1px; line-height: 1; }
  .brand-line { color: #fff; font-weight: 700; font-size: 17px; letter-spacing: 3px; }
  .brand-phone { color: #fff; font-weight: 700; font-size: 17px; letter-spacing: 1px; }
  .brand-square {
    position: absolute; right: 18px; top: 18px; width: 14px; height: 14px; background: var(--accent-green);
  }
  .holder-name {
    position: absolute; left: 40px; top: 200px;
    color: var(--navy); font-weight: 700; font-size: 26px; letter-spacing: 1px;
    text-transform: uppercase;
  }
  .contact-list {
    position: absolute; left: 40px; top: 244px;
    list-style: none; color: var(--ink); font-size: 15px; line-height: 22px;
  }
  .contact-list b { display: inline-block; width: 20px; font-weight: 700; }
  .base-bar {
    position: absolute; left: 0; right: 0; top: 322px; height: 26px;
    background: var(--bar);
  }

  /* Back */
  .service-list {
    position: absolute; left: 40px; top: 120px;
    list-style: none; color: var(--ink); font-size: 19px; line-height: 29px;
  }
  .service-list li { display: flex; align-items: center; gap: 10px; }
  .service-list svg { width: 16px; height: 16px; flex: none; }
  .rope {
    position: absolute; left: 528px; top: 0; width: 2px; height: 150px; background: var(--figure);
  }
  .abseiler {
    position: absolute; left: 420px; top: 120px; width: 230px; height: 190px;
    background: radial-gradient(ellipse at 50% 50%, rgba(60,70,80,0.55) 0%, rgba(60,70,80,0.15) 70%, transparent 100%);
    border-radius: 40%;
  }
</style>
</head>
<body>
<main class="sheet">

  <section class="card card-front" aria-label="Card front">
    <div class="sky-band"></div>
    <div class="brand-block">
      <span class="brand-square"></span>
      <span class="brand-name">GLAZORIA</span>
      <span class="brand-line">SERVICES</span>
      <span class="brand-phone">1300 452 967</span>
    </div>
    <h1 class="holder-name">dean marlow</h1>
    <ul class="contact-list">
      <li><b>M</b>0438 602 917</li>
      <li><b>E</b>dean@glazoria.net.au</li>
      <li><b>W</b>www.glazoria.net.au</li>
    </ul>
    <div class="base-bar"></div>
  </section>

  <section class="card card-back" aria-label="Card back">
    <ul class="service-list">
      <li><svg viewBox="0 0 16 16"><path d="M2 8.5l4 4 8-9" fill="none" stroke="var(--tick)" stroke-width="2.6"/></svg>window cleaning</li>
      <li><svg viewBox="0 0 16 16"><path d="M2 8.5l4 4 8-9" fill="none" stroke="var(--tick)" stroke-width="2.6"/></svg>high pressure cleaning</li>
      <li><svg viewBox="0 0 16 16"><path d="M2 8.5l4 4 8-9" fill="none" stroke="var(--tick)" stroke-width="2.6"/></svg>building washdowns</li>
      <li><svg viewBox="0 0 16 16"><path d="M2 8.5l4 4 8-9" fill="none" stroke="var(--tick)" stroke-width="2.6"/></svg>gutter cleaning</li>
      <li><svg viewBox="0 0 16 16"><path d="M2 8.5l4 4 8-9" fill="none" stroke="var(--tick)" stroke-width="2.6"/></svg>difficult access specialist</li>
      <li><svg viewBox="0 0 16 16"><path d="M2 8.5l4 4 8-9" fill="none" stroke="var(--tick)" stroke-width="2.6"/></svg>abseiling</li>
      <li><svg viewBox="0 0 16 16"><path d="M2 8.5l4 4 8-9" fill="none" stroke="var(--tick)" stroke-width="2.6"/></svg>elevated work platforms</li>
      <li><svg viewBox="0 0 16 16"><path d="M2 8.5l4 4 8-9" fill="none" stroke="var(--tick)" stroke-width="2.6"/></svg>commercial/domestic/high-rise</li>
    </ul>
    <div class="rope"></div>
    <div class="abseiler" role="img" aria-label="Silhouette of a window cleaner abseiling on a rope with a bucket"></div>
  </section>

</main>
</body>
</html>
```